Brightwell Audiology Centre - is state of the art audiology clinic and needs a business card design

the card should be oriented in 'portrait' mode and have a clinic logo. The card should be double sided, with logo on the front and my details on the other side of the card

We would also like to use a tagline of 'Experts in Hearing Care'

Clinic

```html
<!DOCTYPE html>
<html lang="en">
<head>
<meta charset="utf-8">
<title>Brightwell Audiology Centre – Business Card</title>
<link rel="stylesheet" href="https://fonts.googleapis.com/css2?family=Lato:wght@400;700&display=swap">
<style>
  :root {
    --bg: #e9e7e4;
    --card: #ffffff;
    --sky: #74c0f2;
    --sky-deep: #4aa8e8;
    --grey: #8a8a8a;
    --ink: #1c1c1c;
  }
  * { box-sizing: border-box; margin: 0; padding: 0; }
  html, body { width: 1200px; height: 625px; overflow: hidden; }
  body {
    background: var(--bg);
    font-family: "Lato", sans-serif;
    position: relative;
  }
  .card {
    position: absolute;
    top: 32px;
    width: 330px;
    height: 560px;
    background: var(--card);
    box-shadow: 0 6px 18px rgba(0,0,0,.18);
    overflow: hidden;
  }
  .card--front { left: 190px; }
  .card--back { left: 680px; }
  .card__bands { position: absolute; inset: 0; }
  .card__bands path { fill: var(--sky); }

  /* Front */
  .brand {
    position: absolute;
    left: 40px;
    top: 190px;
    display: flex;
    align-items: center;
    gap: 18px;
  }
  .brand__dot {
    width: 46px; height: 46px;
    border-radius: 50%;
    background: var(--sky);
    flex: none;
  }
  .brand__name {
    font-weight: 700;
    font-size: 31px;
    line-height: 1.02;
    letter-spacing: 1px;
    color: var(--grey);
    text-transform: uppercase;
  }
  .tagline {
    position: absolute;
    left: 0; right: 0;
    top: 345px;
    text-align: center;
    font-weight: 700;
    font-size: 13.5px;
    letter-spacing: 4px;
    color: var(--sky);
    text-transform: uppercase;
  }

  /* Back */
  .person {
    position: absolute;
    right: 22px;
    top: 50px;
    text-align: right;
  }
  .person__name {
    font-weight: 700;
    font-size: 22px;
    color: var(--sky-deep);
    text-transform: uppercase;
  }
  .person__creds {
    display: inline-block;
    margin-top: 4px;
    padding: 2px 12px;
    border-radius: 12px;
    background: var(--sky);
    color: #fff;
    font-weight: 700;
    font-size: 14px;
  }
  .person__role {
    margin-top: 6px;
    font-size: 15px;
    line-height: 1.15;
    color: var(--grey);
  }
  .contact-tab {
    position: absolute;
    left: 0; top: 208px;
    width: 50px; height: 180px;
    background: var(--sky);
    border-radius: 0 14px 14px 0;
  }
  .contact-tab svg { display: block; margin: 12px auto 0; }
  .contact-list {
    position: absolute;
    left: 70px; top: 222px;
    list-style: none;
    font-size: 14px;
    color: var(--ink);
  }
  .contact-list li { height: 33px; }
  .contact-list .address { line-height: 1.45; height: auto; margin-top: 2px; }
</style>
</head>
<body>

<section class="card card--front" aria-label="Card front">
  <svg class="card__bands" width="330" height="560" viewBox="0 0 330 560">
    <path d="M80 0 H330 V14 H150 Q132 14 120 7 Q108 0 80 0 Z"/>
    <path d="M0 552 H190 Q215 552 228 544 Q242 535 262 535 H330 V560 H0 Z"/>
  </svg>
  <div class="brand">
    <span class="brand__dot"></span>
    <span class="brand__name">Brightwell<br>Audiology<br>Centre</span>
  </div>
  <p class="tagline">Experts in Hearing Care</p>
</section>

<section class="card card--back" aria-label="Card back">
  <svg class="card__bands" width="330" height="560" viewBox="0 0 330 560">
    <path d="M80 0 H330 V18 H150 Q132 18 120 9 Q108 0 80 0 Z"/>
    <path d="M0 530 H60 Q82 530 94 541 Q106 552 128 552 H330 V560 H0 Z"/>
  </svg>

  <div class="person">
    <h1 class="person__name">Dr Arjun Mehra</h1>
    <span class="person__creds">AuD. MASLP. MAudSA.CCP</span>
    <p class="person__role">Chief Audiologist &amp;<br>Speech Language Pathologist</p>
  </div>

  <div class="contact-tab" aria-hidden="true">
    <svg width="22" height="22" viewBox="0 0 22 22" fill="none" stroke="#fff" stroke-width="1.8">
      <path d="M3 7 Q11 2 19 7 L17 10 L14 9 L14 7 Q11 6 8 7 L8 9 L5 10 Z" fill="#fff"/>
      <rect x="5" y="11" width="12" height="8" rx="1.5"/>
    </svg>
    <svg width="22" height="24" viewBox="0 0 22 24" fill="none" stroke="#fff" stroke-width="1.8">
      <rect x="5" y="2" width="12" height="20" rx="2"/>
      <circle cx="11" cy="18.5" r="1" fill="#fff"/>
    </svg>
    <svg width="24" height="20" viewBox="0 0 24 20" fill="none" stroke="#fff" stroke-width="1.8">
      <rect x="2" y="3" width="20" height="14" rx="1"/>
      <path d="M2 3 L12 11 L22 3"/>
    </svg>
    <svg width="24" height="24" viewBox="0 0 24 24" fill="none" stroke="#fff" stroke-width="1.8">
      <circle cx="12" cy="12" r="9"/>
      <ellipse cx="12" cy="12" rx="4" ry="9"/>
      <path d="M3 12 H21"/>
    </svg>
    <svg width="20" height="24" viewBox="0 0 20 24" fill="#fff">
      <path d="M10 2 C5 2 2 5.5 2 9.5 C2 15 10 22 10 22 C10 22 18 15 18 9.5 C18 5.5 15 2 10 2 Z M10 6.5 A3 3 0 1 1 10 12.5 A3 3 0 1 1 10 6.5 Z"/>
    </svg>
  </div>

  <ul class="contact-list">
    <li class="phone">0836 2457810</li>
    <li class="mobile">9812450736</li>
    <li class="email">arjunmehra@mailbox.in</li>
    <li class="web">www.brightwellaudiology.in</li>
    <li class="address">F 4 Lotus Arcade, Station Road,<br>Dharwad - 580 001. (Karnataka)</li>
  </ul>
</section>

</body>
</html>
```